Radio Service company needs ad for trade publication

Airwave Allies provides sales, content, production, technology, and promotion products and services to radio stations to help increase sales and solutions to improve operations and reduce costs. We are looking for a creative ad (sizes 720x250, 300x250, 728x180) with a theme around "MASTER YOUR 2024 BUDGET with AIRWAVE ALLIES". Categories we have products/services to help them get budget into alignment. (1) Sales (2) Content & Programming (3) Technology (4) Production & Imaging (5) Promotions & Marketing (6) Support Services
"Don't go into the new year with an Unrealistic Budget.....We can Help!"

```html
<!DOCTYPE html>
<html lang="en">
<head>
<meta charset="utf-8">
<title>Master Your 2024 Budget with Airwave Allies</title>
<link rel="stylesheet" href="https://fonts.googleapis.com/css2?family=Poppins:wght@500;600;700;800;900&display=swap">
<style>
:root{
  --board:#3a3939;
  --navy:#253a8c;
  --blue:#0a8ef0;
  --orange:#fb9a06;
  --sky:#bfe3fc;
  --white:#ffffff;
}
*{margin:0;padding:0;box-sizing:border-box}
html,body{width:1067px;height:1200px;overflow:hidden;background:var(--board)}
body{position:relative;font-family:"Poppins",sans-serif;color:var(--navy)}
.ad{position:absolute;overflow:hidden;background:linear-gradient(180deg,var(--sky) 0%,#e6f4fe 40%,var(--white) 70%);box-shadow:10px 12px 14px rgba(0,0,0,.45)}
.ad > *{position:absolute}
.headline{font-weight:900;white-space:nowrap;line-height:1;color:var(--navy)}
.headline .year{color:var(--orange)}
.headline .budget{color:var(--blue)}
.with-badge{border-radius:50%;background:var(--orange);display:flex;align-items:center;justify-content:center}
.with-badge span{font-weight:900;color:var(--navy);transform:rotate(-18deg);letter-spacing:.5px}
.brand{font-weight:700;color:var(--blue);line-height:.95;white-space:nowrap;text-align:center}
.tagline{font-weight:700;white-space:nowrap;color:var(--navy)}
.service{transform:translateX(-50%);text-align:center}
.service svg{display:block;margin:0 auto}
.service p{font-weight:700;white-space:nowrap;line-height:1.2;color:var(--navy)}
.footer-band{left:0;right:0;bottom:0;background:var(--navy);color:var(--white);font-weight:500;display:flex;align-items:center}
.footer-band p{white-space:nowrap}
.footer-band em{font-style:normal;font-weight:800;color:var(--orange)}

/* square ad */
.ad-square{left:326px;top:57px;width:406px;height:338px}
.ad-square .headline{left:11px;font-size:32px;letter-spacing:-.5px}
.ad-square .h1{top:15px}
.ad-square .h2{top:53px}
.ad-square .with-badge{left:237px;top:47px;width:36px;height:36px}
.ad-square .with-badge span{font-size:9px}
.ad-square .brand{left:282px;top:38px;width:110px;font-size:19px}
.ad-square .tagline{left:12px;top:103px;font-size:11px;letter-spacing:3.4px}
.ad-square .service p{font-size:9.5px;letter-spacing:2px;margin-top:4px}
.ad-square .footer-band{height:59px;padding-left:31px;font-size:11.5px;letter-spacing:3.2px;line-height:1.4}

/* wide ad */
.ad-wide{left:42px;top:462px;width:975px;height:338px}
.ad-wide .headline{font-size:64px;letter-spacing:6.5px}
.ad-wide .h1{left:26px;top:14px}
.ad-wide .h2{left:36px;top:75px}
.ad-wide .with-badge{left:564px;top:76px;width:70px;height:70px}
.ad-wide .with-badge span{font-size:19px}
.ad-wide .brand{left:652px;top:52px;width:300px;font-size:56px}
.ad-wide .tagline{left:35px;top:154px;font-size:16px;letter-spacing:3.8px}
.ad-wide .service p{font-size:13px;letter-spacing:4px;margin-top:12px}
.ad-wide .footer-band{height:48px;justify-content:center;font-size:15px;letter-spacing:4.5px}

/* banner ad */
.ad-banner{left:36px;top:859px;width:986px;height:243px}
.ad-banner .headline{left:20px;top:18px;font-size:52px;letter-spacing:-.8px}
.ad-banner .with-badge{left:757px;top:24px;width:58px;height:58px}
.ad-banner .with-badge span{font-size:16px}
.ad-banner .brand{left:822px;top:20px;width:150px;font-size:27px}
.ad-banner .tagline{left:82px;top:76px;font-size:18.5px;letter-spacing:5px}
.ad-banner .service p{font-size:13px;letter-spacing:4px;margin-top:12px}
.ad-banner .footer-band{height:45px;justify-content:center;font-size:15px;letter-spacing:4.5px}
</style>
</head>
<body>

<svg width="0" height="0" style="position:absolute" aria-hidden="true">
  <defs>
    <symbol id="icon-sales" viewBox="0 0 40 40">
      <circle cx="20" cy="20" r="18" fill="#fff" stroke="#253a8c" stroke-width="1.6"/>
      <text x="16" y="26" font-family="Poppins,sans-serif" font-weight="800" font-size="15" fill="#0a8ef0" text-anchor="middle">$</text>
      <path d="M25 28V12M22 15l3-3 3 3" fill="none" stroke="#253a8c" stroke-width="1.6"/>
    </symbol>
    <symbol id="icon-content" viewBox="0 0 40 40">
      <circle cx="20" cy="20" r="18" fill="#fff" stroke="#253a8c" stroke-width="1.6"/>
      <path d="M12 10h11l4 4v16H12z" fill="none" stroke="#0a8ef0" stroke-width="1.5"/>
      <path d="M15 16h8M15 19h8M15 22h6M15 25h5" stroke="#0a8ef0" stroke-width="1.3"/>
      <path d="M20 28l9-9 2 2-9 9-3 1z" fill="#fff" stroke="#253a8c" stroke-width="1.4"/>
    </symbol>
    <symbol id="icon-tech" viewBox="0 0 40 40">
      <circle cx="20" cy="20" r="18" fill="#fff" stroke="#253a8c" stroke-width="1.6"/>
      <rect x="14" y="14" width="12" height="12" fill="none" stroke="#0a8ef0" stroke-width="1.5"/>
      <path d="M17 14V9M20 14V8M23 14V9M17 26v5M20 26v6M23 26v5M14 17H9M14 20H8M14 23H9M26 17h5M26 20h6M26 23h5" stroke="#0a8ef0" stroke-width="1.3"/>
    </symbol>
    <symbol id="icon-production" viewBox="0 0 40 40">
      <circle cx="20" cy="20" r="18" fill="#fff" stroke="#253a8c" stroke-width="1.6"/>
      <path d="M20 10l2.4 6 6.4-1-4.3 5 4.3 5-6.4-1L20 30l-2.4-6-6.4 1 4.3-5-4.3-5 6.4 1z" fill="#0a8ef0"/>
      <circle cx="11" cy="28" r="1.3" fill="#253a8c"/><circle cx="30" cy="11" r="1.3" fill="#253a8c"/>
    </symbol>
    <symbol id="icon-promo" viewBox="0 0 40 40">
      <circle cx="20" cy="20" r="18" fill="#fff" stroke="#253a8c" stroke-width="1.6"/>
      <path d="M10 18h4l10-6v16l-10-6h-4z" fill="none" stroke="#0a8ef0" stroke-width="1.5"/>
      <path d="M14 22l2 6h3l-2-6" fill="none" stroke="#253a8c" stroke-width="1.3"/>
      <path d="M27 16l3-2M27 20h4M27 24l3 2" stroke="#253a8c" stroke-width="1.3"/>
    </symbol>
    <symbol id="icon-support" viewBox="0 0 40 40">
      <circle cx="20" cy="20" r="18" fill="#fff" stroke="#253a8c" stroke-width="1.6"/>
      <path d="M11 22v-3a9 9 0 0 1 18 0v3" fill="none" stroke="#0a8ef0" stroke-width="1.5"/>
      <rect x="9" y="19" width="4" height="7" rx="1.5" fill="#0a8ef0"/>
      <rect x="27" y="19" width="4" height="7" rx="1.5" fill="#0a8ef0"/>
      <path d="M15 20a5 4 0 1 1 4 4l-3 2 .5-3A4 4 0 0 1 15 20z" fill="none" stroke="#253a8c" stroke-width="1.3"/>
    </symbol>
  </defs>
</svg>

<!-- Square ad -->
<section class="ad ad-square">
  <h1 class="headline h1">MASTER YOUR</h1>
  <div class="headline h2"><span class="year">2024</span> BUDGET</div>
  <div class="with-badge"><span>WITH</span></div>
  <div class="brand">AIRWAVE<br>ALLIES</div>
  <h2 class="tagline">WAYS TO GET YOUR BUDGET INTO ALIGNMENT</h2>
  <div class="service" style="left:73px;top:131px"><svg width="34" height="34"><use href="#icon-sales"/></svg><p>SALES</p></div>
  <div class="service" style="left:204px;top:131px"><svg width="34" height="34"><use href="#icon-content"/></svg><p>CONTENT &amp;<br>PROGRAMMING</p></div>
  <div class="service" style="left:336px;top:131px"><svg width="34" height="34"><use href="#icon-tech"/></svg><p>TECHNOLOGY</p></div>
  <div class="service" style="left:73px;top:203px"><svg width="34" height="34"><use href="#icon-production"/></svg><p>PRODUCTION<br>&amp; IMAGING</p></div>
  <div class="service" style="left:204px;top:203px"><svg width="34" height="34"><use href="#icon-promo"/></svg><p>PROMOTIONS<br>&amp; MARKETING</p></div>
  <div class="service" style="left:336px;top:203px"><svg width="34" height="34"><use href="#icon-support"/></svg><p>SUPPORT<br>SERVICES</p></div>
  <div class="footer-band"><p>DON'T GO INTO THE NEW YEAR WITH AN<br>UNREALISTIC BUDGET.....<em>WE CAN HELP!</em></p></div>
</section>

<!-- Wide ad -->
<section class="ad ad-wide">
  <h1 class="headline h1">MASTER YOUR</h1>
  <div class="headline h2"><span class="year">2024</span> <span class="budget">BUDGET</span></div>
  <div class="with-badge"><span>WITH</span></div>
  <div class="brand">AIRWAVE<br>ALLIES</div>
  <h2 class="tagline">WAYS TO GET YOUR BUDGET INTO ALIGNMENT</h2>
  <div class="service" style="left:67px;top:196px"><svg width="39" height="39"><use href="#icon-sales"/></svg><p>SALES</p></div>
  <div class="service" style="left:228px;top:196px"><svg width="39" height="39"><use href="#icon-content"/></svg><p>CONTENT &amp;<br>PROGRAMMING</p></div>
  <div class="service" style="left:393px;top:196px"><svg width="39" height="39"><use href="#icon-tech"/></svg><p>TECHNOLOGY</p></div>
  <div class="service" style="left:568px;top:196px"><svg width="39" height="39"><use href="#icon-production"/></svg><p>PRODUCTION<br>&amp; IMAGING</p></div>
  <div class="service" style="left:728px;top:196px"><svg width="39" height="39"><use href="#icon-promo"/></svg><p>PROMOTIONS<br>&amp; MARKETING</p></div>
  <div class="service" style="left:893px;top:196px"><svg width="39" height="39"><use href="#icon-support"/></svg><p>SUPPORT<br>SERVICES</p></div>
  <div class="footer-band"><p>DON'T GO INTO THE NEW YEAR WITH AN UNREALISTIC BUDGET.....<em>WE CAN HELP!</em></p></div>
</section>

<!-- Banner ad -->
<section class="ad ad-banner">
  <h1 class="headline">MASTER YOUR <span class="year">2024</span> <span class="budget">BUDGET</span></h1>
  <div class="with-badge"><span>WITH</span></div>
  <div class="brand">AIRWAVE<br>ALLIES</div>
  <h2 class="tagline">WAYS TO GET YOUR BUDGET INTO ALIGNMENT</h2>
  <div class="service" style="left:65px;top:112px"><svg width="39" height="39"><use href="#icon-sales"/></svg><p>SALES</p></div>
  <div class="service" style="left:223px;top:112px"><svg width="39" height="39"><use href="#icon-content"/></svg><p>CONTENT &amp;<br>PROGRAMMING</p></div>
  <div class="service" style="left:398px;top:112px"><svg width="39" height="39"><use href="#icon-tech"/></svg><p>TECHNOLOGY</p></div>
  <div class="service" style="left:571px;top:112px"><svg width="39" height="39"><use href="#icon-production"/></svg><p>PRODUCTION<br>&amp; IMAGING</p></div>
  <div class="service" style="left:738px;top:112px"><svg width="39" height="39"><use href="#icon-promo"/></svg><p>PROMOTIONS<br>&amp; MARKETING</p></div>
  <div class="service" style="left:904px;top:112px"><svg width="39" height="39"><use href="#icon-support"/></svg><p>SUPPORT<br>SERVICES</p></div>
  <div class="footer-band"><p>DON'T GO INTO THE NEW YEAR WITH AN UNREALISTIC BUDGET.....<em>WE CAN HELP!</em></p></div>
</section>

</body>
</html>
```